Website Design for Luxury Product

Are you tired of the "same-old-same-old"?
Would you like to make a difference?
Do you want to make your mark as a designer and work on a full and cool project?
If you answered "YES" to any of the questions above ... keep on reading. We've been looking for you!
Our cigar company www.velmorsmokes.com is in need of a new website design.
The look-and-feel needs to ooze luxury, be clean, and exciting.
Our goal is to have people visiting our website walk away and:
1. Understand that we are a high end, luxury cigar company
2. Feel a rapport and excitement with our company
3. Establish credibility
4. Have the visitor want to join our monthly VIP cigar club
Our logo is enclosed below
Frequently Asked Questions:
1. Who Is Your Target Market and What Are Your Demographics?
Our target market is 100% is the US and primarily males between the ages of 33 and 65.
Our target market are successful professionals like investment advisers, bankers, accountants, doctors, and entrepreneurs with a high disposable income.
Our audience has the ability to purchase just about anything they would like but prefer to purchase the highest quality items and don't mind paying a premium for this.
The website must give the visitor confidence that we are the "real thing" and that we are the best-of-the-best.
2. What Will The Website Be Hosted On?
The website will either be hosted as a stand alone website using Control Panel or on a WordPress Site.
3. What Font Should I Use For the Website?
Our standard font is the Gotham Family of Fonts.
4. What Colors Should the Website Use?
Surprise us.
Our goal is to have the website that is modern, hip, cool and oozes luxury.
5. What Look and Feel Should I Use?
Take a look at our newly designed logo which is attached as a file. We are after a look that is modern, clean, and luxurious.
If you think you have the "right stuff" we'd love to hear from you with your design.
Harold and Brian
Target Market(s)
Industry/Entity Type
Social Club
Coding
Coded - Design and coding required
Number of Pages Required
5+ page
Font styles to use
Other font styles liked:
- Gotham Family of Fonts
Requirements
Must have
- My project must have a home page and supporting pages with a consistent them that is
- Modern
- Luxurious
- Establishes Credibility
- For the content to use please look to our website with the existing wording.
Nice to have
- Use your imagination on this one.
Should not have
- Our project should not have a look and feel that is ornate and complicated. An example of this is our existing logo which can be found on our website www.velmorsmokes.com
- We have moved away from this look.

```html
<!DOCTYPE html>
<html lang="en">
<head>
<meta charset="utf-8">
<title>Velmor Cigars</title>
<link href="https://fonts.googleapis.com/css2?family=Montserrat:wght@400;600;700;800&family=Open+Sans:wght@400;600&display=swap" rel="stylesheet">
<style>
:root{
  --orange:#e8760f;
  --dark:#1d1d1d;
  --darker:#141414;
  --panel:#232323;
  --frame:#555;
  --light:#e9e9e9;
  --white:#fff;
  --grey:#8a8a8a;
  --text:#333;
}
*{margin:0;padding:0;box-sizing:border-box}
html,body{width:1200px;height:2862px;overflow:hidden}
body{position:relative;font-family:'Montserrat',sans-serif;background:var(--white);color:var(--text)}
.abs{position:absolute}
.header{left:0;top:0;width:1200px;height:110px;background:var(--white)}
.label{font-size:15px;font-weight:700;letter-spacing:1.5px;color:#777}
.live-phone{left:76px;top:56px;font-size:16px;font-weight:700;color:#222;display:flex;align-items:center;gap:10px}
.dot-icon{width:26px;height:26px;border-radius:50%;background:var(--orange);display:flex;align-items:center;justify-content:center}
.brand{left:450px;top:30px;width:300px;text-align:center;font-size:30px;font-weight:700;letter-spacing:4px;color:#111}
.search{left:910px;top:59px;width:221px;height:31px;background:#e8e8e8;border:1px solid #ccc}
.search span{position:absolute;left:14px;top:9px;font-size:10px;color:#999;font-style:italic}
.search-btn{position:absolute;right:-1px;top:-1px;width:31px;height:31px;background:var(--orange);display:flex;align-items:center;justify-content:center}
.hero{left:0;top:110px;width:1200px;height:586px;background:linear-gradient(100deg,#2a1e17 0%,#5a4436 30%,#9a8b80 45%,#3b3532 60%,#151515 100%)}
.hero-rule{left:0;top:696px;width:1200px;height:5px;background:var(--orange)}
.nav{left:76px;top:134px;display:flex;gap:0;font-size:16px;font-weight:700;color:var(--white);letter-spacing:.5px}
.nav a{position:absolute;white-space:nowrap;color:var(--white);text-decoration:none}
.nav a.active{color:var(--orange)}
.nav-dots{left:78px;top:164px;display:flex;gap:6px}
.nav-dots i{width:7px;height:7px;border-radius:50%;background:var(--white)}
.btn{background:var(--orange);color:var(--white);font-weight:700;font-size:15px;letter-spacing:1px;display:flex;align-items:center;justify-content:center;box-shadow:0 3px 0 #9c4c05}
.login{left:1026px;top:124px;width:102px;height:46px;font-size:16px}
.hero-kicker{left:679px;top:326px;font-size:24px;font-weight:700;color:var(--orange)}
.hero-title{left:677px;top:362px;font-size:38px;font-weight:800;color:var(--white);line-height:44px;letter-spacing:2px}
.hero-cta{left:677px;top:471px;width:195px;height:46px}
.arrow{width:44px;height:44px;border-radius:50%;background:var(--orange);display:flex;align-items:center;justify-content:center;top:388px}
.welcome{left:0;top:701px;width:1200px;height:544px;background:var(--dark)}
.section-title{border-left:6px solid var(--orange);padding-left:14px;font-weight:700;color:var(--white);letter-spacing:2px;line-height:1.15}
.section-title .small{font-size:24px;display:block}
.section-title .big{font-size:30px;display:block;color:var(--orange)}
.card{border:5px solid var(--frame);background:var(--panel)}
.card-accent{height:7px;background:var(--orange)}
.card h3{font-size:16px;font-weight:700;color:#ddd;letter-spacing:1px;margin-bottom:10px}
.card p{font-size:15px;font-weight:600;line-height:23px;color:#888}
.card a{color:var(--orange);font-weight:700;text-decoration:none}
.quote-band{left:0;top:1245px;width:1200px;height:154px;background:var(--light)}
.quote-brand{left:70px;top:1262px;height:124px;border-left:6px solid #111;padding-left:24px;display:flex;align-items:center;font-size:30px;font-weight:700;letter-spacing:3px;color:#111}
.quote{left:328px;top:1266px;width:830px;font-size:25px;font-weight:800;color:#111;letter-spacing:2px;line-height:42px}
.quote cite{display:block;font-style:normal;color:var(--orange);font-size:24px;letter-spacing:1.5px}
.party{left:0;top:1399px;width:1200px;height:433px;background:var(--dark)}
.party .big{color:var(--white)}
.party .big em{color:var(--orange);font-style:normal}
.photo{top:1534px;width:300px;height:231px}
.vip-band{left:0;top:1832px;width:1200px;height:153px;background:var(--light)}
.vip-title{left:72px;top:1874px;border-left:6px solid #111;padding-left:14px;font-weight:800;letter-spacing:1.5px;line-height:1.2}
.vip-title .small{font-size:24px;color:#111;display:block}
.vip-title .big{font-size:30px;color:var(--orange);display:block}
.vip-text{left:527px;top:1852px;width:620px;font-size:20px;font-weight:700;color:#111;line-height:29px;letter-spacing:.5px}
.vip-btn{top:1921px;height:35px;font-size:14px}
.contact-item{left:76px;display:flex;gap:22px;font-size:15px;font-weight:700;color:#333;line-height:29px}
.contact-item svg{flex:none;margin-top:6px}
.divider{left:76px;width:361px;height:2px;background:#ddd}
.field{left:502px;width:624px;border:1px solid #ccc;background:var(--white);font-family:'Open Sans',sans-serif;font-size:15px;color:#aaa;padding:18px 14px}
.submit{left:502px;top:2318px;width:194px;height:50px;font-size:16px}
.footer{left:0;top:2418px;width:1200px;height:375px;background:var(--dark)}
.foot-h{top:2455px;font-size:25px;font-weight:700;color:var(--white);letter-spacing:2px}
.foot-p{font-family:'Open Sans',sans-serif;font-size:14px;line-height:25px;color:#888}
.social{top:2671px;width:44px;height:44px;background:#2e2e2e;border:1px solid #3c3c3c}
.post{left:349px;width:250px;font-family:'Open Sans',sans-serif;font-size:14px;font-weight:600;color:var(--white);line-height:23px}
.post.hl{color:var(--orange)}
.post small{display:block;font-size:11px;color:#888;font-weight:400;margin-top:6px}
.trails{left:626px;top:2504px;width:248px;list-style:none;font-family:'Open Sans',sans-serif;font-size:14px;color:#999}
.trails li{height:41px;line-height:40px;border-bottom:1px solid #3a3a3a}
.trails li::before{content:"›";color:var(--orange);font-weight:700;font-size:20px;margin-right:6px}
.thumb{width:68px;height:68px}
.copyright{left:0;top:2793px;width:1200px;height:69px;background:var(--darker);text-align:center;line-height:69px;font-size:14px;color:#666;letter-spacing:1.5px}
</style>
</head>
<body>
<header class="abs header">
  <div class="abs label" style="left:76px;top:30px">LIVE HELP</div>
  <div class="abs live-phone">
    <span class="dot-icon"><svg width="14" height="14" viewBox="0 0 24 24"><path fill="#fff" d="M6.6 10.8a15 15 0 0 0 6.6 6.6l2.2-2.2c.3-.3.7-.4 1-.2 1.1.4 2.3.6 3.6.6.6 0 1 .4 1 1V20c0 .6-.4 1-1 1A17 17 0 0 1 3 4c0-.6.4-1 1-1h3.5c.6 0 1 .4 1 1 0 1.3.2 2.5.6 3.6.1.3 0 .7-.2 1z"/></svg></span>
    (+000) 555 010 2030
  </div>
  <div class="abs brand">VELMOR</div>
  <div class="abs label" style="left:910px;top:30px">SEARCH HERE</div>
  <div class="abs search"><span>SEARCH HERE</span>
    <div class="search-btn"><svg width="14" height="14" viewBox="0 0 24 24"><circle cx="10" cy="10" r="6" fill="none" stroke="#111" stroke-width="3"/><path d="M14.5 14.5 21 21" stroke="#111" stroke-width="3"/></svg></div>
  </div>
</header>

<section class="abs hero" role="img" aria-label="Photo of a woman in a dark hat exhaling smoke while holding an electronic cigarette"></section>
<nav class="abs nav">
  <a class="active" style="left:0">HOME</a>
  <a style="left:80px">VIP CLUB ENROLLMENT</a>
  <a style="left:323px">OUR STORY</a>
  <a style="left:458px">TASTE PROFILE</a>
  <a style="left:628px">THE VELMOR BLEND</a>
  <a style="left:847px">CONTACT</a>
</nav>
<div class="abs nav-dots"><i></i><i></i><i></i><i></i></div>
<div class="abs btn login">LOGIN</div>
<div class="abs hero-kicker">velmor cigarette products</div>
<h1 class="abs hero-title">ALTERNATIVE TO<br>SMOKING</h1>
<div class="abs btn hero-cta">GET STARTED</div>
<div class="abs arrow" style="left:20px"><svg width="16" height="16" viewBox="0 0 16 16"><path d="M11 2 5 8l6 6" fill="none" stroke="#fff" stroke-width="3"/></svg></div>
<div class="abs arrow" style="left:1138px"><svg width="16" height="16" viewBox="0 0 16 16"><path d="m5 2 6 6-6 6" fill="none" stroke="#fff" stroke-width="3"/></svg></div>
<div class="abs hero-rule"></div>

<section class="abs welcome"></section>
<h2 class="abs section-title" style="left:72px;top:738px"><span class="small">WELCOME TO THE</span><span class="big">VELMOR CIGAR</span></h2>
<div class="abs card-accent" style="left:260px;top:834px;width:106px"></div>
<div class="abs card" style="left:72px;top:841px;width:493px;height:330px;padding:5px;background:#fff">
  <div role="img" aria-label="Photo of a cigar resting on a black lacquered presentation box" style="width:100%;height:100%;background:linear-gradient(160deg,#f4f4f4 0%,#3a3a3a 45%,#1a1a1a 70%,#efefef 100%)"></div>
</div>
<div class="abs card-accent" style="left:780px;top:834px;width:114px"></div>
<div class="abs card" style="left:576px;top:841px;width:550px;height:170px;padding:12px 18px">
  <h3>VELMOR CIGAR</h3>
  <p>Our fellow brothers and sisters of the leaf, welcome you've arrived.<br>At Velmor Cigars our mission is to elevate your your enjoyment of cigars and life's special moments<br><a>Read more</a></p>
</div>
<div class="abs card-accent" style="left:650px;top:1012px;width:118px"></div>
<div class="abs card" style="left:576px;top:1019px;width:273px;height:152px;padding:12px 18px">
  <h3>VIP MEMBERSHIP</h3>
  <p style="font-size:14px;line-height:21px">You Are About To Embark On A Journey Unlike Any You Have Ever Experienced.<br><a>Read more</a></p>
</div>
<div class="abs card" style="left:857px;top:1019px;width:269px;height:152px;padding:12px 18px">
  <h3>A TASTE LIKE NONE OTHER</h3>
  <p style="font-size:14px;line-height:21px">Combine art with science seven rare and special tobacco leaves from four countries. <a>Read more</a></p>
</div>

<section class="abs quote-band"></section>
<div class="abs quote-brand">VELMOR</div>
<blockquote class="abs quote">"WE MAKE A LIVING BY WHAT WE GET, BUT WE MAKE A LIFE BY WHAT WE GIVE."<cite>-- Arthur Pendle</cite></blockquote>

<section class="abs party"></section>
<h2 class="abs section-title" style="left:72px;top:1440px"><span class="small" style="font-size:24px">SHOW YOUR IMAGES</span><span class="big"><span style="color:#fff">YOUR PARTY </span>PICTURES</span></h2>
<div class="abs photo" role="img" aria-label="Close-up photo of cigar smoke being exhaled" style="left:0;background:linear-gradient(135deg,#8d8582,#c9c3c0 55%,#6a625e)"></div>
<div class="abs photo" role="img" aria-label="Photo of a guest relaxing in a leather armchair with a cigar" style="left:300px;background:linear-gradient(135deg,#2a211b,#8a6a45 50%,#3a2c20)"></div>
<div class="abs photo" role="img" aria-label="Photo of hands cutting a cigar over an ashtray" style="left:600px;background:linear-gradient(135deg,#0f1c2a,#6b4b35 50%,#101820)"></div>
<div class="abs photo" role="img" aria-label="Photo of a lit cigar held between fingers" style="left:900px;background:linear-gradient(135deg,#3b2a22,#a58977 50%,#2c221d)"></div>

<section class="abs vip-band"></section>
<h2 class="abs vip-title"><span class="small">VELMOR OFFER</span><span class="big">VIP CLUB ENROLLMENT</span></h2>
<p class="abs vip-text">You Are About To Embark On A Journey Unlike Any You Have Ever Experienced.</p>
<div class="abs btn vip-btn" style="left:527px;width:148px">READ MORE</div>
<div class="abs btn vip-btn" style="left:698px;width:128px">GET STARTED</div>

<div class="abs contact-item" style="top:2046px">
  <svg width="14" height="18" viewBox="0 0 14 18"><path d="M7 0a7 7 0 0 0-7 7c0 5 7 11 7 11s7-6 7-11a7 7 0 0 0-7-7zm0 10a3 3 0 1 1 0-6 3 3 0 0 1 0 6z" fill="#333"/></svg>
  <div>Velmor Cigars by Grand Oeuvre Estates<br>2271 Marlow Lane, Cedar Bluff, FL 32000</div>
</div>
<div class="abs divider" style="top:2126px"></div>
<div class="abs contact-item" style="top:2150px">
  <svg width="20" height="14" viewBox="0 0 20 14"><rect x="1" y="1" width="18" height="12" fill="none" stroke="#333" stroke-width="2"/><path d="m1 1 9 7 9-7" fill="none" stroke="#333" stroke-width="2"/></svg>
  <div>vip@velmorsmokes.com<br>www.velmorsmokes.com</div>
</div>
<div class="abs divider" style="top:2231px"></div>
<div class="abs contact-item" style="top:2258px">
  <svg width="16" height="16" viewBox="0 0 24 24"><path fill="#333" d="M6.6 10.8a15 15 0 0 0 6.6 6.6l2.2-2.2c.3-.3.7-.4 1-.2 1.1.4 2.3.6 3.6.6.6 0 1 .4 1 1V20c0 .6-.4 1-1 1A17 17 0 0 1 3 4c0-.6.4-1 1-1h3.5c.6 0 1 .4 1 1 0 1.3.2 2.5.6 3.6.1.3 0 .7-.2 1z"/></svg>
  <div>1 (800) 555 - 0199</div>
</div>
<div class="abs field" style="top:2028px;height:56px">Name</div>
<div class="abs field" style="top:2104px;height:56px">Email</div>
<div class="abs field" style="top:2181px;height:122px;padding-top:12px">Message</div>
<div class="abs btn submit">SUBMIT</div>

<footer class="abs footer"></footer>
<h4 class="abs foot-h" style="left:72px">ABOUT</h4>
<h4 class="abs foot-h" style="left:349px">LATEST POSTS</h4>
<h4 class="abs foot-h" style="left:626px">TRAILS</h4>
<h4 class="abs foot-h" style="left:900px">GALLERY</h4>
<p class="abs foot-p" style="left:72px;top:2512px;width:240px">Integer imperdiet aliquet velit, vel tinci dunt lectus dictum sed. Cura bitur dign issim ut massa vel tinci dunt. Nullam imperdiet pharetra.</p>
<div class="abs social" style="left:76px"></div>
<div class="abs social" style="left:130px"></div>
<div class="abs social" style="left:183px"></div>
<div class="abs social" style="left:236px"></div>
<div class="abs post" style="top:2507px">Completely Re-Engineer superior fast and fit<small>12 April 2015</small></div>
<div class="abs post hl" style="top:2590px">Completely Re-Engineer fast and fit superior<small>12 April 2015</small></div>
<div class="abs post" style="top:2673px">Completely Re-Engineer is fast and fit superior<small>12 April 2015</small></div>
<ul class="abs trails">
  <li>Dolor sit amet, consectr scing</li>
  <li>Vel Tincidunt lectus</li>
  <li>Curabitur Dignissim Ut</li>
  <li>Libero Mauris Luctus</li>
  <li>Fetiam Convallis</li>
  <li>Donec a Scelerisque</li>
</ul>
<div class="abs thumb" role="img" aria-label="Gallery photo of an e-cigarette" style="left:900px;top:2511px;background:linear-gradient(135deg,#3a3a3a,#9a8a80)"></div>
<div class="abs thumb" role="img" aria-label="Gallery photo of e-cigarette kit" style="left:979px;top:2511px;background:linear-gradient(135deg,#eee,#b33)"></div>
<div class="abs thumb" role="img" aria-label="Gallery photo of e-cigarette in hand" style="left:1057px;top:2511px;background:linear-gradient(135deg,#4a6a3a,#c9b89a)"></div>
<div class="abs thumb" role="img" aria-label="Gallery photo of coloured e-cigarettes" style="left:900px;top:2591px;background:linear-gradient(135deg,#5a5a7a,#c9a04a)"></div>
<div class="abs thumb" role="img" aria-label="Gallery photo of e-cigarette devices" style="left:979px;top:2591px;background:linear-gradient(135deg,#ddd,#555)"></div>
<div class="abs thumb" role="img" aria-label="Gallery photo of green e-cigarette" style="left:1057px;top:2591px;background:linear-gradient(135deg,#6a9a4a,#ccc)"></div>
<div class="abs thumb" role="img" aria-label="Gallery photo of blue e-cigarette" style="left:900px;top:2671px;background:linear-gradient(135deg,#4a7ab0,#ddd)"></div>
<div class="abs thumb" role="img" aria-label="Gallery photo of silver e-cigarettes" style="left:979px;top:2671px;background:linear-gradient(135deg,#f2f2f2,#777)"></div>
<div class="abs thumb" role="img" aria-label="Gallery photo of e-cigarette with purple light" style="left:1057px;top:2671px;background:linear-gradient(135deg,#7a4ab0,#c9a070)"></div>
<div class="abs copyright">Copyright 2016 - VELMOR. All Rights Reserved.</div>
</body>
</html>
```